Pool bar in traditional boutique hotel in Crete needs a menu

We need a menu design for the new pool bar in a traditional boutique hotel called Kalyvi Dranessa based in Chania, Crete in Greece. We serve homemade desserts, pies, salads, cocktails and fresh juices, all made with local or our products. We would like to see a menu happy and simple like us and our guests.

Target Market(s)

Families, old and young couples, gay couples

Industry/Entity Type

Boutique

```html
<!DOCTYPE html>
<html lang="en">
<head>
<meta charset="utf-8">
<title>Kalyvi Dranessa – Pool Bar Menu</title>
<link rel="stylesheet" href="https://fonts.googleapis.com/css2?family=Carlito:wght@400;700&display=swap">
<style>
  :root {
    --page: #ffffff;
    --menu-red: #a60000;
    --menu-red-deep: #4d0000;
    --rule: #c42a2a;
    --title-red: #8e0000;
    --soft-pink: #e87a7a;
    --ink-white: #ffffff;
    --night: #0b0b0b;
    --night-mid: #262626;
    --seal-red: #b00000;
  }
  * { margin: 0; padding: 0; box-sizing: border-box; }
  html, body { width: 1200px; height: 928px; overflow: hidden; background: var(--page); }
  body { position: relative; font-family: "Carlito", "Calibri", sans-serif; }

  .menu-card, .brand-card { position: absolute; top: 22px; height: 884px; overflow: hidden; }

  /* Menu side */
  .menu-card { left: 22px; width: 561px; background: var(--menu-red); }
  .hotel-name {
    position: absolute; right: 36px; font-size: 50px; font-weight: 700;
    color: var(--title-red); white-space: nowrap;
    text-shadow: 1px 1px 0 rgba(255,120,120,.45), -1px -1px 1px rgba(0,0,0,.45);
  }
  .menu-card .hotel-name { top: 44px; }
  .hotel-place { position: absolute; right: 38px; font-size: 23px; color: var(--soft-pink); white-space: nowrap; }
  .menu-card .hotel-place { top: 120px; }
  .section-title { position: absolute; left: 57px; top: 190px; font-size: 30px; color: var(--ink-white); }
  .menu-list { position: absolute; left: 58px; width: 489px; list-style: none; }
  .menu-list.first { top: 236px; }
  .menu-list.second { top: 416px; }
  .menu-item {
    display: flex; justify-content: space-between; align-items: center;
    height: 29px; padding: 0 8px 0 16px; font-size: 16.5px; color: var(--ink-white);
    border-bottom: 1px solid var(--rule);
  }
  .menu-item:last-child { border-bottom: none; }
  .menu-footer { position: absolute; left: 0; bottom: 0; width: 561px; height: 260px; }
  .footer-name {
    position: absolute; left: 0; width: 561px; top: 690px; text-align: center;
    font-size: 30px; font-weight: 700; color: var(--ink-white);
  }

  /* Brand side */
  .brand-card {
    left: 618px; width: 560px;
    background: radial-gradient(ellipse at 30% 20%, var(--night-mid) 0%, var(--night) 70%);
  }
  .flourish-area {
    position: absolute; left: 60px; top: 0; width: 500px; height: 640px;
    background: radial-gradient(ellipse at 70% 35%, rgba(150,150,150,.28) 0%, rgba(110,110,110,.12) 45%, rgba(0,0,0,0) 75%);
  }
  .seal { position: absolute; left: 140px; top: 288px; width: 270px; height: 290px; }
  .seal-name {
    position: absolute; left: 140px; top: 416px; width: 270px; text-align: center;
    font-size: 30px; font-weight: 700; color: var(--ink-white);
  }
  .tagline {
    position: absolute; left: 0; width: 576px; top: 596px; text-align: center;
    font-size: 25px; color: var(--ink-white); letter-spacing: .3px;
  }
  .brand-card .hotel-name { top: 716px; right: 44px; }
  .brand-card .hotel-place { top: 792px; right: 44px; }
  .phone { position: absolute; right: 44px; top: 830px; font-size: 50px; color: var(--ink-white); white-space: nowrap; line-height: 1; }
</style>
</head>
<body>

<section class="menu-card" aria-label="Dessert menu">
  <h1 class="hotel-name">Kalyvi Dranessa</h1>
  <p class="hotel-place">Chania, Crete in Greece</p>
  <h2 class="section-title">Desserts</h2>
  <ul class="menu-list first">
    <li class="menu-item"><span>Tahitian Vanilla Ice</span><span>$10</span></li>
    <li class="menu-item"><span>Cream</span><span>$10</span></li>
    <li class="menu-item"><span>Roasted Almonds</span><span>$10</span></li>
    <li class="menu-item"><span>Chocolate Sauce</span><span>$10</span></li>
  </ul>
  <ul class="menu-list second">
    <li class="menu-item"><span>Tahitian Vanilla Ice</span><span>$10</span></li>
    <li class="menu-item"><span>Cream</span><span>$10</span></li>
    <li class="menu-item"><span>Roasted Almonds</span><span>$10</span></li>
    <li class="menu-item"><span>Chocolate Sauce</span><span>$10</span></li>
  </ul>
  <svg class="menu-footer" viewBox="0 0 561 260" aria-hidden="true">
    <defs>
      <radialGradient id="footShadow" cx="50%" cy="50%" r="50%">
        <stop offset="0%" stop-color="#000" stop-opacity=".55"/>
        <stop offset="100%" stop-color="#000" stop-opacity="0"/>
      </radialGradient>
    </defs>
    <path d="M0 260 L0 183 Q280 110 561 168 L561 260 Z" fill="var(--menu-red-deep)"/>
    <ellipse cx="280" cy="222" rx="70" ry="10" fill="url(#footShadow)"/>
  </svg>
  <p class="footer-name">Kalyvi Dranessa</p>
</section>

<section class="brand-card" aria-label="Hotel cover">
  <div class="flourish-area" role="img" aria-label="Grey swirling floral ornament over a dark textured background"></div>
  <svg class="seal" viewBox="0 0 270 290" aria-hidden="true">
    <defs>
      <radialGradient id="sealShadow" cx="50%" cy="50%" r="50%">
        <stop offset="0%" stop-color="#000" stop-opacity=".9"/>
        <stop offset="100%" stop-color="#000" stop-opacity="0"/>
      </radialGradient>
    </defs>
    <ellipse cx="135" cy="248" rx="75" ry="12" fill="url(#sealShadow)"/>
    <circle cx="135" cy="134" r="134" fill="var(--seal-red)"/>
  </svg>
  <p class="seal-name">Kalyvi Dranessa</p>
  <p class="tagline">TRADITIONAL BOUTIQUE HOTEL</p>
  <h2 class="hotel-name">Kalyvi Dranessa</h2>
  <p class="hotel-place">Chania, Crete in Greece</p>
  <p class="phone">555 0142 7788</p>
</section>

</body>
</html>
```